Searchable website that will contain information about sites for Bright Harbor Roster.

Once a search is performed the website will show the following information per site:
Title, Description, Screenshot of the site. I'm thinking three items per row.

Number of Pages Required

1 page

Font styles to use
Sans Serif

Colors
ffffff
3176b5

```html
<!DOCTYPE html>
<html lang="en">
<head>
<meta charset="utf-8">
<title>Bright Harbor Roster</title>
<link href="https://fonts.googleapis.com/css2?family=Open+Sans:wght@400;600;700&family=Roboto+Condensed:wght@400;700&display=swap" rel="stylesheet">
<style>
:root{
  --brand:#3176b5;
  --teal:#17a79a;
  --white:#ffffff;
  --ink:#222;
  --muted:#555;
  --star:#e8892b;
  --grey-band:#f0f0f0;
  --footer:#0c0c0c;
}
*{margin:0;padding:0;box-sizing:border-box}
html,body{width:1200px;height:4091px;overflow:hidden}
body{font-family:"Open Sans",sans-serif;color:var(--ink);background:var(--white);position:relative}
.abs{position:absolute}
.topbar{left:0;top:0;width:1200px;height:44px;background:var(--brand);color:var(--white);font-size:14px}
.topbar .contact{left:88px;top:12px;display:flex;gap:14px;align-items:center}
.topbar .auth{right:88px;top:12px}
.topbar svg{vertical-align:-2px;margin-right:4px}
.header{left:0;top:44px;width:1200px;height:114px;background:var(--white)}
.logo{left:88px;top:38px;font-family:"Open Sans",sans-serif;font-weight:700;font-size:31px;color:var(--brand);letter-spacing:-.5px}
.nav{right:88px;top:48px;display:flex;gap:38px;font-size:16px;color:#333}
.nav .active{color:var(--brand)}
.hero{left:0;top:158px;width:1200px;height:529px;background:linear-gradient(100deg,#6d7f8c 0%,#9fb0bc 35%,#8aa0b0 60%,#5f7d94 100%)}
.hero-photo{left:90px;top:20px;width:430px;height:509px;background:linear-gradient(180deg,#3d4b57,#566876);border-radius:4px}
.hero h1{left:540px;top:165px;width:520px;text-align:center;font-family:"Roboto Condensed",sans-serif;font-weight:700;font-size:50px;color:#0d2d4a}
.hero .tag{left:540px;top:245px;width:520px;text-align:center;font-size:19px;font-weight:600;color:#0d2030}
.search{left:537px;top:292px;width:560px;height:60px;display:flex}
.search .field{flex:1;background:var(--white);font-size:16px;color:#555;padding:18px 20px}
.search .btn{width:86px;background:var(--teal);color:var(--white);font-weight:700;font-size:17px;text-align:center;line-height:60px}
.dots{left:1160px;top:225px;display:flex;flex-direction:column;gap:10px}
.dots span{width:9px;height:9px;border-radius:50%;background:rgba(255,255,255,.7)}
.dots span.on{background:var(--brand)}
.sec-title{left:0;width:1200px;text-align:center;font-size:38px;color:#222}
.card{width:328px;height:445px;background:var(--white);box-shadow:0 2px 10px rgba(0,0,0,.22)}
.card .shot{position:absolute;left:14px;top:27px;width:300px;height:191px}
.card h3{position:absolute;left:24px;top:240px;font-size:21px;font-weight:400;color:#222}
.card .stars{position:absolute;left:24px;top:280px;display:flex;gap:3px}
.card .stars i{width:13px;height:13px;background:var(--star)}
.card .stars i.off{background:#cfcfcf}
.card p{position:absolute;left:24px;top:310px;width:285px;font-size:14px;line-height:26px;color:#444}
.card .more{position:absolute;left:24px;top:390px;font-size:14px;color:var(--brand)}
.pager{left:362px;top:2350px;display:flex;gap:7px;font-size:14px}
.pager span{height:28px;min-width:28px;padding:0 8px;line-height:28px;text-align:center;background:#eee;border:1px solid #ddd;color:#333}
.pager span.cur{background:var(--teal);color:var(--white);border-color:var(--teal)}
.about{left:0;top:2482px;width:1200px;height:591px;background:var(--grey-band)}
.about .photo{left:592px;top:141px;width:515px;height:328px;background:linear-gradient(120deg,#e6e6e6,#cfd4d8 60%,#b8c6d6)}
.about .frame{left:82px;top:125px;width:551px;height:365px;border:2px solid var(--brand);background:rgba(255,255,255,.85)}
.about h2{left:122px;top:160px;font-size:38px;font-weight:400}
.about p{left:120px;top:222px;width:440px;font-size:14px;line-height:28px;color:#444;text-align:justify}
.about .btn{left:120px;top:424px;background:#1f5597;color:var(--white);font-size:14px;padding:4px 18px;border-radius:14px}
.play{left:822px;top:274px;width:58px;height:58px;border-radius:50%;background:var(--white);box-shadow:0 0 0 6px rgba(255,255,255,.5)}
.tcard{width:453px;height:227px;background:var(--white);border:2px solid #ddd;box-shadow:0 2px 8px rgba(0,0,0,.1)}
.tcard .avatar{position:absolute;left:-32px;top:52px;width:117px;height:117px;border-radius:50%;background:linear-gradient(135deg,#7a8a5a,#4c5a3a)}
.tcard h4{position:absolute;left:110px;top:48px;font-size:17px;font-weight:400}
.tcard .q{position:absolute;right:42px;top:22px;font-family:Georgia,serif;font-size:80px;line-height:80px;color:var(--teal);font-weight:700}
.tcard p{position:absolute;left:110px;top:80px;width:310px;font-size:14px;line-height:26px;color:#555}
.tcard .by{position:absolute;right:54px;top:170px;font-size:16px;color:#c0392b}
.footer{left:0;top:3605px;width:1200px;height:486px;background:var(--footer);border-top:11px solid var(--brand);color:var(--white)}
.footer h5{font-size:18px;font-weight:400;letter-spacing:.5px}
.footer .col{top:104px}
.footer ul{list-style:none;margin-top:20px;font-size:15px;line-height:33px}
.footer .info{font-size:13px;line-height:18px;margin-top:22px;padding-left:28px;position:relative}
.footer .info b{font-weight:700;font-size:15px;display:block}
.footer .info svg{position:absolute;left:0;top:2px}
.footer input{display:block;width:311px;height:40px;margin-bottom:8px;border:1px solid #ccc;padding:0 16px;font-family:inherit;font-size:15px;color:#333}
.footer .send{width:126px;height:33px;background:var(--brand);color:var(--white);text-align:center;line-height:33px;font-size:17px;margin-top:12px}
.copy{left:0;top:420px;width:1200px;text-align:center;font-size:13px;color:#999}
</style>
</head>
<body>
<div class="abs topbar">
  <div class="abs contact">
    <span><svg width="14" height="14" viewBox="0 0 24 24"><path fill="#fff" d="M6.6 10.8a15 15 0 0 0 6.6 6.6l2.2-2.2c.3-.3.7-.4 1-.2 1.1.4 2.3.6 3.6.6.6 0 1 .4 1 1V20c0 .6-.4 1-1 1A17 17 0 0 1 3 4c0-.6.4-1 1-1h3.5c.6 0 1 .4 1 1 0 1.3.2 2.5.6 3.6.1.3 0 .7-.2 1z"/></svg>555-204-7761</span>
    <span>|</span>
    <span><svg width="14" height="12" viewBox="0 0 24 18"><rect width="24" height="18" rx="2" fill="#fff"/><path d="M1 1l11 9 11-9" stroke="#3176b5" stroke-width="2" fill="none"/></svg>hello@brightharbor.example</span>
  </div>
  <div class="abs auth">Login &nbsp;|&nbsp; Sign Up</div>
</div>

<header class="abs header">
  <div class="abs logo">Bright Harbor Roster</div>
  <nav class="abs nav"><span class="active">Home</span><span>About us</span><span>Services</span><span>FAQ &amp; Extras</span><span>Blog</span><span>Contact Us</span></nav>
</header>

<section class="abs hero">
  <div class="abs hero-photo" role="img" aria-label="Photo of a smiling man holding a tablet"></div>
  <h1 class="abs">Online Entrepreneurs</h1>
  <div class="abs tag">Neque porro quisquam est qui dolorem ipsum quia dolor</div>
  <div class="abs search"><div class="field">Search entrepreneurs</div><div class="btn">Search</div></div>
  <div class="abs dots"><span></span><span class="on"></span><span></span><span></span><span></span></div>
</section>

<h2 class="abs sec-title" style="top:805px;font-weight:400">Result</h2>

<div class="abs card" style="left:87px;top:886px"><div class="shot" role="img" aria-label="Digital marketing site screenshot" style="background:linear-gradient(135deg,#5fd3e0,#bfeff2)"></div><h3>Dolorem Ipsum</h3><div class="stars"><i></i><i></i><i></i><i class="off"></i><i class="off"></i></div><p>It is long established fact that reader will be distracted the readable the point of using Lorem Ipsumis that established.</p><span class="more">Read More »</span></div>
<div class="abs card" style="left:431px;top:886px"><div class="shot" role="img" aria-label="Startup business site screenshot" style="background:linear-gradient(135deg,#2a1a6e,#6a3fb8)"></div><h3>Porro quisquam</h3><div class="stars"><i></i><i></i><i></i><i class="off"></i><i class="off"></i></div><p>It is long established fact that reader will be distracted the readable the point of using Lorem Ipsumis that established.</p><span class="more">Read More »</span></div>
<div class="abs card" style="left:777px;top:886px"><div class="shot" role="img" aria-label="Business apps site screenshot" style="background:linear-gradient(135deg,#3f3fc8,#e8e8f6)"></div><h3>Dolor sit amet</h3><div class="stars"><i></i><i></i><i></i><i class="off"></i><i class="off"></i></div><p>It is long established fact that reader will be distracted the readable the point of using Lorem Ipsumis that established.</p><span class="more">Read More »</span></div>

<div class="abs card" style="left:87px;top:1361px"><div class="shot" role="img" aria-label="Business apps site screenshot" style="background:linear-gradient(110deg,#ffffff 40%,#3a3ad0)"></div><h3>Porro quisquam</h3><div class="stars"><i></i><i></i><i></i><i class="off"></i><i class="off"></i></div><p>It is long established fact that reader will be distracted the readable the point of using Lorem Ipsumis that established.</p><span class="more">Read More »</span></div>
<div class="abs card" style="left:431px;top:1361px"><div class="shot" role="img" aria-label="Web design site screenshot" style="background:linear-gradient(135deg,#7a3fa8,#e26b4a 70%,#f0a050)"></div><h3>Dolor sit amet</h3><div class="stars"><i></i><i></i><i></i><i class="off"></i><i class="off"></i></div><p>It is long established fact that reader will be distracted the readable the point of using Lorem Ipsumis that established.</p><span class="more">Read More »</span></div>
<div class="abs card" style="left:777px;top:1361px"><div class="shot" role="img" aria-label="Digital marketing site screenshot" style="background:linear-gradient(135deg,#ffffff,#6a5ad8 70%,#3a2aa8)"></div><h3>Dolorem Ipsum</h3><div class="stars"><i></i><i></i><i></i><i class="off"></i><i class="off"></i></div><p>It is long established fact that reader will be distracted the readable the point of using Lorem Ipsumis that established.</p><span class="more">Read More »</span></div>

<div class="abs card" style="left:87px;top:1835px"><div class="shot" role="img" aria-label="Web development workspace screenshot" style="background:linear-gradient(135deg,#2f3a44,#55626c)"></div><h3>Dolorem Ipsum</h3><div class="stars"><i></i><i></i><i></i><i class="off"></i><i class="off"></i></div><p>It is long established fact that reader will be distracted the readable the point of using Lorem Ipsumis that established.</p><span class="more">Read More »</span></div>
<div class="abs card" style="left:431px;top:1835px"><div class="shot" role="img" aria-label="Think outside the box site screenshot" style="background:linear-gradient(135deg,#1e8fe0,#5cc0f0)"></div><h3>Porro quisquam</h3><div class="stars"><i></i><i></i><i></i><i class="off"></i><i class="off"></i></div><p>It is long established fact that reader will be distracted the readable the point of using Lorem Ipsumis that established.</p><span class="more">Read More »</span></div>
<div class="abs card" style="left:777px;top:1835px"><div class="shot" role="img" aria-label="Web design and development site screenshot" style="background:linear-gradient(135deg,#3a2ab8,#c03a8a)"></div><h3>Dolor sit amet</h3><div class="stars"><i></i><i></i><i></i><i class="off"></i><i class="off"></i></div><p>It is long established fact that reader will be distracted the readable the point of using Lorem Ipsumis that established.</p><span class="more">Read More »</span></div>

<div class="abs pager"><span>Prev</span><span class="cur">1</span><span>2</span><span>3</span><span>4</span><span>5</span><span>6</span><span>...</span><span>22</span><span>Next</span></div>

<section class="abs about">
  <div class="abs photo" role="img" aria-label="Photo of a woman with a sketched rocket on a brick wall"></div>
  <div class="abs frame"></div>
  <h2 class="abs">About Us</h2>
  <p class="abs">It is a long established fact that a reader will be distracted by the readable content of a page when looking at its layout. The point of using Lorem Ipsum is that it has a more-or-less normal distribution of letters, as opposed to using 'Content here, content here', making it look like readable English. Many desktop publishing packages and web page editors now use Lorem Ipsum as their default model text, and a search</p>
  <span class="abs btn">Read More</span>
  <div class="abs play"><svg width="58" height="58" viewBox="0 0 58 58"><path d="M23 18l18 11-18 11z" fill="#3176b5"/></svg></div>
</section>

<h2 class="abs sec-title" style="top:3180px;font-weight:400">Testimonials</h2>
<div class="abs tcard" style="left:123px;top:3283px"><div class="avatar" role="img" aria-label="Portrait of a client"></div><h4>Neque porro quisquam</h4><div class="q">“</div><p>The point of using Lorem Ipsum is that it has a more-or-less normal distribution of letters, as opposed to using 'Content</p><span class="by">-&nbsp;&nbsp; Marta</span></div>
<div class="abs tcard" style="left:644px;top:3283px"><div class="avatar" role="img" aria-label="Portrait of a client" style="background:linear-gradient(135deg,#8a6a4a,#4a3a2a)"></div><h4>Dolorem ipsum quia dolor</h4><div class="q">“</div><p>The point of using Lorem Ipsum is that it has a more-or-less normal distribution of letters, as opposed to using 'Content</p><span class="by">- Amet</span></div>

<footer class="abs footer">
  <div class="abs col" style="left:96px">
    <h5>CONTACT US</h5>
    <div class="info"><svg width="18" height="20" viewBox="0 0 24 24"><path d="M12 2a7 7 0 0 0-7 7c0 5 7 13 7 13s7-8 7-13a7 7 0 0 0-7-7z" fill="none" stroke="#fff" stroke-width="2"/><circle cx="12" cy="9" r="2.5" fill="#fff"/></svg><b>ADDRESS</b>48 Quay Lane, Suite 3<br>Portview, OR 97000</div>
    <div class="info"><svg width="18" height="18" viewBox="0 0 24 24"><path fill="none" stroke="#fff" stroke-width="2" d="M6.6 10.8a15 15 0 0 0 6.6 6.6l2.2-2.2c.3-.3.7-.4 1-.2 1.1.4 2.3.6 3.6.6.6 0 1 .4 1 1V20c0 .6-.4 1-1 1A17 17 0 0 1 3 4c0-.6.4-1 1-1h3.5c.6 0 1 .4 1 1 0 1.3.2 2.5.6 3.6.1.3 0 .7-.2 1z"/></svg><b>PHONE NUMBER</b>555.310.4482</div>
  </div>
  <div class="abs col" style="left:390px"><h5>ABOUT</h5><ul><li>Home</li><li>About Us</li><li>Services</li><li>How it works</li></ul></div>
  <div class="abs col" style="left:567px"><h5>RESOURCES</h5><ul><li>Support</li><li>Why Us</li><li>Testimonials</li><li>FAQ</li></ul></div>
  <div class="abs col" style="left:796px"><h5>GET IN TOUCH</h5>
    <div style="margin-top:20px"><input value="Your Name"><input value="Email address"><input value="Phone"></div>
    <div class="send">SEND</div>
  </div>
  <div class="abs copy">© 2018 Company Name All right reserved</div>
</footer>
</body>
</html>
```